Reeds Movie Teaser Poster

I'm a director looking for a teaser poster (standard portrait poster dimensions-ratio of 27x40 in.) for an independent film, entitled Reeds The film is a road story (drama), so please feature a highway/car image (not a nice car-a beaten-up sedan along the lines of a 90's-era Venkor Astrelle), and preferably a southwestern-USA sunset motif. The colors should be bold and dramatic, leaning on reds and oranges. Example: http://www.plaverno.com/images/lf/panoKESTRIDGE.jpg

A good reference point would be the 'Ash Over Water' "Everything ends" ad campaign: http://cdn2.quilbyphoto.net/4471/4462842537_da8f4a7e21.jpg

Industry/Entity Type

Movie

Requirements
Must have
• Please feature the title Reeds in the largest font. then, in smaller font, the catchphrase Hold Fast. Go Slow. Live On. Let Go. And finally, in the smallest font, the words Coming Soon. The catchphrase and Coming Soon should be clustered together and separated from the title

Please use a conservative and elegant serif typeface
Nice to have
• None

```html
<!DOCTYPE html>
<html lang="en">
<head>
<meta charset="utf-8">
<title>Reeds — Teaser Poster</title>
<link rel="stylesheet" href="https://fonts.googleapis.com/css2?family=Bodoni+Moda:wght@400;700;900&family=Playfair+Display:wght@700;900&display=swap">
<style>
  :root {
    --sky-top: #d8562a;
    --sky-mid: #ee8a34;
    --sky-low: #f4a546;
    --rock-light: #c0522c;
    --rock-deep: #8c2a14;
    --rock-shadow: #5e1a0c;
    --road: #2b1d18;
    --road-deep: #1c1210;
    --ink-light: #fbf3ea;
    --ink-rust: #6a1a0f;
  }
  html, body {
    margin: 0;
    padding: 0;
    width: 810px;
    height: 1200px;
    overflow: hidden;
    background: var(--road-deep);
  }
  .poster {
    position: relative;
    width: 810px;
    height: 1200px;
    overflow: hidden;
  }
  .poster__scene {
    position: absolute;
    inset: 0;
    background: linear-gradient(180deg,
      var(--sky-top) 0px,
      var(--sky-mid) 180px,
      var(--sky-low) 330px,
      var(--rock-light) 360px,
      var(--rock-deep) 520px,
      var(--rock-shadow) 690px,
      var(--road) 720px,
      var(--road-deep) 1200px);
  }
  .title-block {
    position: absolute;
    left: 147px;
    top: 116px;
    width: 515px;
    height: 126px;
    box-sizing: border-box;
    border-top: 1.5px solid var(--ink-light);
    border-bottom: 1.5px solid var(--ink-light);
    display: flex;
    align-items: center;
    justify-content: center;
  }
  .title {
    margin: 0;
    font-family: "Bodoni Moda", serif;
    font-weight: 400;
    font-size: 134px;
    line-height: 1;
    color: var(--ink-light);
    letter-spacing: 22px;
    padding-left: 22px;
    white-space: nowrap;
  }
  .teaser {
    position: absolute;
    left: 0;
    right: 0;
    top: 996px;
    text-align: center;
  }
  .tagline {
    margin: 0;
    font-family: "Playfair Display", serif;
    font-weight: 900;
    font-size: 40px;
    line-height: 1;
    color: var(--ink-light);
    transform: scaleX(0.68);
    white-space: nowrap;
  }
  .release {
    margin: 6px 0 0;
    font-family: "Bodoni Moda", serif;
    font-weight: 900;
    font-size: 28px;
    line-height: 1;
    letter-spacing: 0.5px;
    color: var(--ink-rust);
  }
</style>
</head>
<body>
  <main class="poster">
    <div class="poster__scene" role="img" aria-label="Photograph of a worn white sedan driving along a winding desert highway through red rock formations under an orange sunset sky"></div>
    <header class="title-block">
      <h1 class="title">REEDS</h1>
    </header>
    <section class="teaser">
      <p class="tagline">HOLD FAST. GO SLOW. LIVE ON. LET GO.</p>
      <p class="release">COMING SOON</p>
    </section>
  </main>
</body>
</html>
```